National Golf Software business needs banner ad designs

Our software company looks after golf clubs throughout the country. Our service specialises in membership billing for the clubs and tries to convince members to change from paying their fees upfront to monthly payment by direct debit. Simple catch cries like "spread the cost of your membership across the whole year", "let us help you make your membership affordable", "Ask you club how to spread the cost of your subs" etc. We are dealing with cost conscious clubs - not the top end of the market - and their members are also cost conscious. No good being too 'high brow'. We are also dealing with older members who are fearful of change and afraid of technology - we need to be safe and reassuring yet a great way to save up front costs. We need probably 5 to 10 banners that can rotate through on our website and on our mobile product.

Target Market(s)

Golfers, typically older and afraid of technology and afraid of direct debit. Existing members of golf clubs who have paid upfront for years and don't understand why they should pay a few dollars extra each month to split their payments. Sometimes their annual fees are quite low ($300 - $400) so they cannot justify the additional $3.50 per month surcharge for splitting their fees.

Industry/Entity Type

Golf Course

Requirements
Must have
• Make the member desire to spread the cost of their annual subscriptions. Safe, reliable, frees up their disposable income. Talk to the club to find out how. Safe and secure. Club administered.
Nice to have
• Option to call us directly on a 1300 582 916 number - they will still need to go back to the club to fill in and lodge the paperwork.
Should not have
• Cheesy, in your face, aggressive

```html
<!DOCTYPE html>
<html lang="en">
<head>
<meta charset="utf-8">
<title>Monthly Membership Banner</title>
<link href="https://fonts.googleapis.com/css2?family=Oswald:wght@400;500;600&display=swap" rel="stylesheet">
<style>
  :root {
    --wood-light: #b07a45;
    --wood-dark: #7a4a22;
    --navy-dark: #14245a;
    --navy-light: #2c4a95;
    --gold: #f2c93a;
    --gold-edge: #d8b24a;
    --white: #ffffff;
    --red: #c3221d;
    --red-dark: #8e1411;
    --green: #8aa23a;
    --green-light: #b5c86a;
    --ink: #2a2a2a;
    --turf-light: #8fbf5a;
    --turf-dark: #2f5a24;
  }
  * { margin: 0; padding: 0; box-sizing: border-box; }
  html, body { width: 1200px; height: 533px; overflow: hidden; }
  body { font-family: "Oswald", sans-serif; background: var(--wood-dark); }

  .canvas { position: relative; width: 1200px; height: 533px; overflow: hidden; }
  .backdrop {
    position: absolute; inset: 0;
    background: linear-gradient(90deg, var(--wood-light), var(--wood-dark) 50%, var(--wood-light));
  }
  .course-photo {
    position: absolute; left: 540px; top: 27px; width: 639px; height: 320px;
    background: linear-gradient(180deg, var(--turf-dark) 0%, #4e7d35 45%, var(--turf-light) 100%);
  }
  .shapes { position: absolute; inset: 0; }

  .headline {
    position: absolute; left: 48px; top: 32px;
    color: var(--white); font-size: 39px; font-weight: 500; letter-spacing: 0.5px; line-height: 1;
  }
  .subline {
    position: absolute; left: 50px; top: 82px;
    color: var(--gold); font-size: 24px; font-weight: 500; letter-spacing: 0.5px; line-height: 1;
  }
  .benefits { position: absolute; left: 50px; top: 170px; list-style: none; width: 480px; }
  .benefits li {
    position: relative; padding-left: 40px; margin-bottom: 12px;
    color: var(--white); font-size: 26px; font-weight: 500; line-height: 1.05;
  }
  .benefits svg { position: absolute; left: 0; top: 4px; width: 26px; height: 22px; }
  .price {
    position: absolute; left: 48px; top: 402px;
    color: var(--gold); font-size: 50px; font-weight: 600; font-style: italic; line-height: 1;
  }
  .price span { font-size: 26px; font-weight: 500; }

  .visit-btn {
    position: absolute; left: 720px; top: 232px; width: 240px; height: 60px;
    background: linear-gradient(180deg, #d9342c, var(--red-dark));
    border-radius: 6px; box-shadow: 0 3px 6px rgba(0,0,0,.4);
    display: flex; align-items: center; justify-content: center; gap: 16px;
    color: var(--white); font-size: 27px; font-weight: 500;
  }
  .visit-btn .divider { width: 2px; height: 34px; background: rgba(255,255,255,.5); }

  .brand { position: absolute; left: 604px; top: 392px; display: flex; align-items: center; gap: 10px; }
  .brand-dot { width: 26px; height: 26px; border-radius: 50%; background: var(--navy-dark); }
  .brand-name { color: var(--navy-dark); font-size: 52px; font-weight: 500; line-height: 1; }
  .brand-tag { position: absolute; left: 604px; top: 454px; color: var(--navy-dark); font-size: 12px; }

  .phone {
    position: absolute; left: 870px; top: 388px; display: flex; align-items: center; gap: 12px;
    color: var(--white); font-size: 36px; font-weight: 500; line-height: 1;
  }
  .phone svg { width: 26px; height: 26px; }
</style>
</head>
<body>
<div class="canvas">
  <div class="backdrop" role="img" aria-label="Warm wooden plank background"></div>
  <div class="course-photo" role="img" aria-label="Photo of golfers on a green fairway lined with trees"></div>

  <svg class="shapes" width="1200" height="533" viewBox="0 0 1200 533">
    <defs>
      <linearGradient id="navy" x1="0" y1="0" x2="1" y2="1">
        <stop offset="0" stop-color="#2c4a95"/>
        <stop offset="1" stop-color="#14245a"/>
      </linearGradient>
    </defs>
    <!-- white lower area -->
    <rect x="540" y="347" width="639" height="160" fill="#ffffff"/>
    <!-- navy panel with chevron edge -->
    <polygon points="21,27 548,27 600,228 565,507 21,507" fill="url(#navy)"/>
    <polyline points="548,27 600,228 565,507" fill="none" stroke="#d8b24a" stroke-width="5"/>
    <!-- green ribbon -->
    <polygon points="800,373 1179,373 1179,453 800,453 826,413" fill="#8aa23a"/>
    <polyline points="815,381 1179,381" stroke="#b5c86a" stroke-width="2" stroke-dasharray="6 4"/>
    <polyline points="815,445 1179,445" stroke="#b5c86a" stroke-width="2" stroke-dasharray="6 4"/>
  </svg>

  <h1 class="headline">LOREM IPSUM DOLAR</h1>
  <p class="subline">SIMPLY DUMMY TEXT</p>

  <ul class="benefits">
    <li><svg viewBox="0 0 26 22"><path d="M2 12 L9 19 L24 3" fill="none" stroke="#f2c93a" stroke-width="4"/></svg>SAFE AND SECURE</li>
    <li><svg viewBox="0 0 26 22"><path d="M2 12 L9 19 L24 3" fill="none" stroke="#f2c93a" stroke-width="4"/></svg>RELIABLE</li>
    <li><svg viewBox="0 0 26 22"><path d="M2 12 L9 19 L24 3" fill="none" stroke="#f2c93a" stroke-width="4"/></svg>CLUB ADMINISTERED</li>
    <li><svg viewBox="0 0 26 22"><path d="M2 12 L9 19 L24 3" fill="none" stroke="#f2c93a" stroke-width="4"/></svg>FREES UP THEIR DISPOSABLE INCOME</li>
  </ul>

  <p class="price">$24.99<span>/ MONTH</span></p>

  <div class="visit-btn">VISIT NOW <span class="divider"></span>
    <svg width="16" height="18" viewBox="0 0 16 18"><polygon points="0,0 16,9 0,18" fill="#ffffff"/></svg>
  </div>

  <div class="brand"><span class="brand-dot"></span><span class="brand-name">TEEPAY</span></div>
  <p class="brand-tag">membership &amp; club software</p>

  <div class="phone">
    <svg viewBox="0 0 24 24"><path d="M6.6 10.8c1.4 2.8 3.8 5.1 6.6 6.6l2.2-2.2c.3-.3.7-.4 1-.2 1.1.4 2.3.6 3.6.6.6 0 1 .4 1 1V20c0 .6-.4 1-1 1C10.6 21 3 13.4 3 4c0-.6.4-1 1-1h3.5c.6 0 1 .4 1 1 0 1.3.2 2.5.6 3.6.1.3 0 .7-.2 1l-2.3 2.2z" fill="#ffffff"/></svg>
    1300 582 916
  </div>
</div>
</body>
</html>
```